Design a Logo and Business Card

I have started a Home Inspection business and would like to have a Logo and Business card designed. I have attached a business card I made myself but I feel it is lacking the designer touch. I have attached my current business card and a DREMO logo which I would like to have on the business card. The business card can have a front and back or just a front whichever works best. My company name is on the attached card. Feel free to let your creative ideas flow. I like blues, greens whites, greys & blacks and I' am open to other colors as well. I'm looking for a classy logo style.
My next steps after this design is to have a website built using the same colors as the logo and business card. I look forward to what you can create.

```html
<!DOCTYPE html>
<html lang="en">
<head>
<meta charset="utf-8">
<title>RK Home Inspections — Business Card</title>
<link href="https://fonts.googleapis.com/css2?family=Arimo:wght@400&family=Questrial&display=swap" rel="stylesheet">
<style>
  :root {
    --backdrop: #d9d7d4;
    --charcoal: #3a3b3d;
    --paper: #ffffff;
    --accent-blue: #1a87bd;
    --ink: #1c1c1c;
    --muted: #9a9a9a;
    --tagline: #8d8f92;
    --badge-red: #d8232a;
  }
  * { box-sizing: border-box; margin: 0; padding: 0; }
  html, body { width: 1200px; height: 792px; overflow: hidden; }
  body {
    background: var(--backdrop);
    position: relative;
    font-family: "Arimo", Arial, sans-serif;
  }
  .card {
    position: absolute;
    top: 241px;
    width: 540px;
    height: 309px;
    display: flex;
    box-shadow: 0 6px 18px rgba(0,0,0,0.18);
    overflow: hidden;
  }
  .card--back { left: 40px; }
  .card--front { left: 620px; }

  /* Back side: contact details */
  .contact-panel {
    flex: 0 0 76%;
    background: var(--paper);
    padding: 34px 30px 30px 34px;
    display: flex;
    flex-direction: column;
  }
  .contact-name { font-size: 19px; color: var(--ink); }
  .contact-title { font-size: 14px; color: var(--accent-blue); margin-top: 2px; }
  .contact-lines { margin-top: 26px; font-size: 16px; color: var(--ink); line-height: 1.5; }
  .registrations { margin-top: auto; font-size: 16px; color: var(--muted); line-height: 1.2; letter-spacing: 0.5px; }
  .accent-stripe { flex: 0 0 2.4%; background: var(--accent-blue); }
  .charcoal-strip { flex: 1; background: var(--charcoal); }

  /* Front side: brand */
  .brand-panel {
    flex: 0 0 76%;
    background: var(--charcoal);
    display: flex;
    flex-direction: column;
    align-items: center;
    justify-content: center;
    gap: 14px;
    padding: 0 20px;
    font-family: "Questrial", "Century Gothic", sans-serif;
  }
  .brand-name {
    display: flex;
    align-items: center;
    gap: 10px;
    color: var(--accent-blue);
    font-size: 22px;
    letter-spacing: 1px;
  }
  .brand-dot { width: 12px; height: 12px; border-radius: 50%; background: var(--accent-blue); }
  .tagline { color: var(--tagline); font-size: 16px; letter-spacing: 0.4px; white-space: nowrap; }
  .badge-panel {
    flex: 1;
    background: var(--paper);
    position: relative;
  }
  .partner-badge {
    position: absolute;
    right: 22px;
    bottom: 40px;
  }
</style>
</head>
<body>
  <section class="card card--back" aria-label="Card back with contact details">
    <div class="contact-panel">
      <p class="contact-name">Name</p>
      <p class="contact-title">Title</p>
      <div class="contact-lines">
        <p>(431)&nbsp; 555-0187</p>
        <p>info@rkhomeinspections.com</p>
      </div>
      <div class="registrations">
        <p>DREMO(BC)&nbsp; #&nbsp; 412</p>
        <p>HLPC#&nbsp; 40531</p>
      </div>
    </div>
    <div class="accent-stripe"></div>
    <div class="charcoal-strip"></div>
  </section>

  <section class="card card--front" aria-label="Card front with brand">
    <div class="brand-panel">
      <div class="brand-name"><span class="brand-dot"></span><span>RK Home Inspections</span></div>
      <p class="tagline">Bringing calm clarity to every home you buy</p>
    </div>
    <div class="accent-stripe"></div>
    <div class="badge-panel">
      <svg class="partner-badge" width="56" height="50" viewBox="0 0 56 50" role="img" aria-label="Partner association badge">
        <rect x="0" y="0" width="56" height="50" fill="var(--badge-red)"/>
      </svg>
    </div>
  </section>
</body>
</html>
```